Vintage poster/postcard for 2011 New Years Eve event with theme 'Lumière Volante'

I have had a major change of mind since the last brief due to my original requirements being too specific. I hope this new brief allows more scope for the designers and I am extending the deadline by 7 days.

For the first time my new business 'Tidewell Gala' is planning an exciting, large scale New Years Eve fundraising event in Hobart Tasmania, Australia. The unique and eclectic theme of the party is 'Lumière Volante' (french for contemporary circus). I require a vintage style poster design (similar to a traditional french advertising poster) that can double as a postcard invitation so it must look good on a smaller scale as well.
Updates

Project Deadline Extended
Reason: My original brief was very specific and I now realise very limiting for the designers. I have changed my mind with the look I want for the vintage poster (more along the lines of the traditional french advertising posters of old) and therefore would like to allow designers extra time to submit a design. Thank you. Jill Barrow Tidewell Gala

Target Market(s)

25-50 yr old professionals prepared to pay premium price for a quality, fresh & fun NYE experience while giving to charity.

Industry/Entity Type

Advertising

Requirements
Must have
• - A heading that reads: Tidewell Gala proudly presents
Lumière Volante
- Text that includes: 2011 New Years Eve Extravanaganza Saturday 31st December and find out more at "www.tidewellgala.example
- A strip left blank at the bottom to include my business logo and others sponsors
- Classic french vintage poster design
- - Plenty of colour but not too fluro
- Something that looks good enough to be framed or sent to a friend
Should not have
• - Picture of Eiffel Tower or any other specific French references
- Any animals

```html
<!DOCTYPE html>
<html lang="en">
<head>
<meta charset="utf-8">
<title>Tidewell Gala — Lumière Volante 2011</title>
<link rel="stylesheet" href="https://fonts.googleapis.com/css2?family=Ewert&display=swap">
<style>
  :root {
    --paper: #ece4c4;
    --paper-shade: #d9d6c4;
    --map-tone: #f3d99a;
    --elephant: #9a5a48;
    --elephant-cap: #c0532c;
    --acrobat: #27427a;
    --furniture: #c9ad7a;
    --tiger: #d9782e;
    --clown: #d9b23a;
    --clown-red: #d2463c;
    --stamp: #e4e0d6;
    --ink: #3a2f2a;
    --strip: #f4efdc;
    --extrude: rgba(60, 60, 60, 0.35);
  }
  * { margin: 0; padding: 0; box-sizing: border-box; }
  html, body { width: 900px; height: 1200px; overflow: hidden; }
  body { background: #ffffff; }

  .poster {
    position: relative;
    width: 900px;
    height: 1200px;
    overflow: hidden;
    background: radial-gradient(ellipse at 40% 45%, var(--paper) 0%, var(--paper-shade) 100%);
    font-family: "Ewert", "Rye", serif;
  }

  .art { position: absolute; display: block; z-index: 1; }
  .art--map {
    left: 60px; top: 300px; width: 600px; height: 600px;
    background: radial-gradient(ellipse at 50% 45%, var(--map-tone) 0%, rgba(243,217,154,0.6) 70%, rgba(243,217,154,0) 100%);
    clip-path: polygon(5% 10%, 40% 4%, 75% 0%, 100% 25%, 96% 70%, 80% 95%, 60% 100%, 30% 90%, 10% 70%, 2% 40%);
  }
  .art--elephant {
    left: 410px; top: 0; width: 490px; height: 290px;
    background: radial-gradient(ellipse at 75% 35%, var(--elephant-cap) 0%, var(--elephant) 45%, rgba(154,90,72,0.85) 100%);
    border-radius: 40% 0 0 60% / 30% 0 0 70%;
  }
  .art--acrobat {
    left: 110px; top: 270px; width: 310px; height: 340px;
    background: linear-gradient(160deg, var(--acrobat) 0%, #3d5a95 55%, #e9d9c4 100%);
    border-radius: 30% 60% 40% 50%;
    opacity: 0.75;
  }
  .art--furniture {
    left: 260px; top: 590px; width: 270px; height: 250px;
    background: linear-gradient(160deg, var(--furniture) 0%, #8c7a5a 60%, #1e1e1e 100%);
    clip-path: polygon(0 10%, 90% 0, 100% 20%, 80% 100%, 40% 90%, 10% 60%);
  }
  .art--tiger {
    left: 600px; top: 540px; width: 300px; height: 460px;
    background: linear-gradient(170deg, #c76e2c 0%, var(--tiger) 45%, #f0e4d4 80%, #a04a26 100%);
    border-radius: 50% 0 40% 60% / 40% 0 40% 50%;
  }
  .art--clowns {
    left: 40px; top: 880px; width: 430px; height: 210px;
    background: linear-gradient(150deg, var(--clown) 0%, #e7c95b 40%, var(--clown-red) 75%, #f3e8d8 100%);
    border-radius: 40% 50% 20% 30%;
  }
  .badge {
    position: absolute; left: -60px; top: 990px; z-index: 1;
    width: 130px; height: 130px; border-radius: 50%;
    background: var(--stamp); border: 4px solid #555;
  }

  .headline {
    position: absolute;
    z-index: 2;
    white-space: nowrap;
    line-height: 1;
    color: transparent;
    -webkit-background-clip: text;
    background-clip: text;
    -webkit-text-stroke: 2px rgba(255,255,255,0.7);
    filter: drop-shadow(5px 5px 0 var(--extrude));
    text-transform: uppercase;
  }
  .headline--host {
    left: 400px; top: 120px;
    font-size: 300px;
    background-image: linear-gradient(90deg, #3bcf9a 0%, #49d640 45%, #7fe030 75%, #27b4e8 100%);
    transform: translate(-50%, -50%) rotate(-3deg) scale(0.42, 0.75);
  }
  .headline--event {
    left: 585px; top: 440px;
    font-size: 220px;
    background-image: linear-gradient(90deg, #f2e000 0%, #b4e020 35%, #38d27a 65%, #1fb8e6 100%);
    transform: translate(-50%, -50%) rotate(-25deg) scale(0.8, 1);
  }
  .headline--theme {
    font-size: 170px;
    background-image: linear-gradient(90deg, #3bd43a 0%, #2fce8a 50%, #3b6fe0 80%, #8a3ad6 100%);
  }
  .headline--theme-a { left: 230px; top: 630px; transform: translate(-50%, -50%) rotate(90deg) scale(0.58, 0.85); }
  .headline--theme-b { left: 85px; top: 670px; transform: translate(-50%, -50%) rotate(90deg) scale(0.62, 0.85); }
  .headline--year {
    left: 700px; top: 890px;
    font-size: 170px;
    background-image: linear-gradient(90deg, #2a8fe0 0%, #7a3ad8 45%, #c92ec2 75%, #e8308c 100%);
    transform: translate(-50%, -50%) rotate(55deg) scale(0.72, 1);
  }

  .tagline {
    position: absolute; z-index: 3;
    left: 40px; top: 232px;
    font-size: 24px;
    color: var(--ink);
    letter-spacing: 2px;
  }
  .details {
    position: absolute; z-index: 3;
    left: 0; right: 0; top: 1092px;
    text-align: center;
    color: var(--ink);
  }
  .details__date { font-size: 20px; letter-spacing: 1px; }
  .details__web { font-size: 16px; margin-top: 6px; letter-spacing: 1px; }

  .sponsor-strip {
    position: absolute; z-index: 3;
    left: 0; right: 0; bottom: 0; height: 50px;
    background: var(--strip);
    border-top: 2px solid var(--ink);
  }
</style>
</head>
<body>
  <main class="poster">
    <div class="art art--map" role="img" aria-label="Vintage map of the island state with town markers"></div>
    <div class="art art--elephant" role="img" aria-label="Vintage circus elephant wearing an ornate red and gold headdress"></div>
    <div class="art art--acrobat" role="img" aria-label="Acrobat in a starry blue costume balancing in a handstand"></div>
    <div class="art art--furniture" role="img" aria-label="Stacked wooden and black chairs used for the balancing act"></div>
    <div class="art art--clowns" role="img" aria-label="Two vintage circus clowns in patterned yellow and striped red costumes"></div>
    <div class="art art--tiger" role="img" aria-label="Vintage illustration of a leaping tiger"></div>
    <div class="badge" aria-hidden="true"></div>

    <h1 class="headline headline--host">Tidewell</h1>
    <p class="tagline">proudly presents</p>
    <p class="headline headline--event">Gala</p>
    <p class="headline headline--theme headline--theme-a">Lumière</p>
    <p class="headline headline--theme headline--theme-b">Volante</p>
    <p class="headline headline--year">2011</p>

    <div class="details">
      <p class="details__date">New Years Eve Extravaganza · Saturday 31st December</p>
      <p class="details__web">find out more at www.tidewellgala.example</p>
    </div>

    <div class="sponsor-strip" aria-hidden="true"></div>
  </main>
</body>
</html>
```